Brackenfold Health Web Page

We need a visually exciting webpage that introduces people to our practice. We are a practice that has both physiotherapy and psychology and we need the page to reflect this. We are also split across two practice locations. We need the page to be able to be updated regularly to include a blog spot and the linking in of our facebook page. There should be tabs to introduce our practitioners with some blurbs about them, a tab for people to be able to contact us, a tab to read about physiotherapy services and a tab to talk about psychology services. If there are other tabs than please include these. We are a practice that has treated world class athlete on a regular basis and see our selves as leaders in the field and the website must reflect this. I do not want basic clip-arty type things that anyone could have, we have to have something that draws people in.
Firstly, thanks everyone for their designs. I have attached some links to some physiotherapy websites that I think contain some interesting information and/or layout, as well as some comments,
Hi all,
Reason: Hi Guys,
We are so very close to finding a great design. I feel that we just need a bit of extra time to be able to clinch where we want to be. Thanks for your fantastic designs :)
Regards,
Oliver and Ruth
- 2 Practice Addresses (details to follow for right applications)
Psychology aspect
Physiotherapy aspect
Ability to update blog

```html
<!DOCTYPE html>
<html lang="en">
<head>
<meta charset="utf-8">
<title>Brackenfold Health</title>
<link href="https://fonts.googleapis.com/css2?family=Arimo:wght@400;700&display=swap" rel="stylesheet">
<style>
  :root {
    --ink: #111111;
    --white: #ffffff;
    --rule: #1a1a1a;
    --nav-divider: #222222;
    --social: #2d3a8c;
    --button: #e4e4e4;
    --section-top: #ffffff;
    --section-bottom: #dcdcdc;
    --card-border: #b9b9b9;
    --card-fill: #fbfbfb;
    --label: #4a4a4a;
    --footer: #4d4d4d;
    --footer-text: #f2f2f2;
  }
  * { box-sizing: border-box; margin: 0; padding: 0; }
  html, body { width: 874px; height: 1200px; overflow: hidden; }
  body {
    font-family: "Arimo", Arial, sans-serif;
    color: var(--ink);
    background: var(--white);
    position: relative;
  }

  /* Header */
  .site-header { position: absolute; inset: 0 0 auto 0; height: 134px; }
  .brand {
    position: absolute; left: 14px; top: 22px;
    font-size: 38px; font-weight: 700; letter-spacing: -0.5px; color: var(--ink);
  }
  .social-link {
    position: absolute; right: 24px; top: 50px;
    width: 24px; height: 24px; background: var(--social);
  }
  .main-nav {
    position: absolute; left: 110px; right: 0; top: 88px; height: 40px;
    display: flex; border-bottom: 2px solid var(--rule);
  }
  .main-nav a {
    flex: none; display: flex; align-items: center; justify-content: center;
    text-align: center; font-size: 15px; line-height: 15px; color: var(--ink);
    text-decoration: none; border-left: 2px solid var(--nav-divider);
  }
  .main-nav a:first-child { border-left: none; }
  .nav-locations { width: 112px; }
  .nav-practitioners { width: 142px; }
  .nav-physio { width: 132px; }
  .nav-psych { width: 130px; }
  .nav-blog { width: 80px; }
  .nav-contact { width: 168px; }

  /* Hero */
  .hero {
    position: absolute; left: 0; right: 0; top: 134px; height: 333px;
    border-top: 3px solid var(--rule); border-bottom: 4px solid var(--rule);
    background: var(--white);
  }
  .hero-photo {
    position: absolute; left: 0; top: 0; width: 484px; height: 326px;
    background: linear-gradient(135deg, #d9d6d4 0%, #f4f2f0 35%, #c9b4a6 60%, #3b3230 100%);
  }
  .hero-tagline {
    position: absolute; left: 346px; top: 32px;
    font-size: 26px; line-height: 30px; color: var(--ink);
  }
  .hero-tagline span { display: block; }
  .hero-tagline span + span { padding-left: 38px; }
  .appointment {
    position: absolute; left: 550px; top: 148px; text-align: left;
  }
  .appointment p { font-size: 25px; }
  .appointment-button {
    display: block; margin: 14px 0 0 134px; width: 132px; height: 44px;
    background: var(--button); border-radius: 4px;
    font-size: 25px; line-height: 44px; text-align: center;
    color: var(--ink); text-decoration: none;
  }

  /* Services */
  .services {
    position: absolute; left: 0; right: 0; top: 467px; height: 594px;
    background: linear-gradient(var(--section-top) 0%, var(--section-bottom) 100%);
  }
  .services-title {
    position: absolute; left: 34px; top: 56px;
    font-size: 28px; font-weight: 400;
  }
  .service-card {
    position: absolute; width: 402px; height: 182px;
    border: 2px solid var(--card-border); border-radius: 16px;
    background: var(--card-fill);
  }
  .card-group { left: 25px; top: 118px; }
  .card-therapy { left: 451px; top: 118px; }
  .card-physio { left: 25px; top: 340px; }
  .card-sports { left: 451px; top: 340px; }
  .service-photo {
    position: absolute; left: 16px; top: 22px; width: 198px; height: 132px;
  }
  .card-therapy .service-photo { left: 0; width: 214px; top: 14px; height: 148px; }
  .card-physio .service-photo { left: 22px; width: 176px; top: 28px; height: 120px; }
  .card-sports .service-photo { left: 22px; width: 176px; top: 28px; height: 120px; }
  .photo-group { background: linear-gradient(160deg, #c7b89d, #8c7a5e 60%, #5b4a3a); }
  .photo-therapy { background: linear-gradient(150deg, #e8e4dc, #b9a47a 55%, #2f2f2f); }
  .photo-physio { background: linear-gradient(160deg, #d9d9d6, #9aa7b4 55%, #3a4a6a); }
  .photo-sports { background: linear-gradient(160deg, #1f2a3c, #4a5a7a 55%, #c9c3bb); }
  .service-label {
    position: absolute; left: 226px; top: 24px; width: 162px; height: 38px;
    background: var(--label); border-radius: 5px;
    color: var(--white); font-size: 15px; line-height: 38px; text-align: center;
    font-weight: 400;
  }
  .service-text {
    position: absolute; left: 232px; top: 76px; width: 160px;
    font-size: 11px; line-height: 13px; font-weight: 700;
  }

  /* Footer */
  .site-footer {
    position: absolute; left: 0; right: 0; bottom: 0; height: 139px;
    background: var(--footer); color: var(--footer-text);
  }
  .footer-nav { position: absolute; left: 14px; top: 16px; display: flex; }
  .footer-nav a {
    color: var(--footer-text); text-decoration: none; font-size: 13px;
    line-height: 15px; text-align: center;
  }
  .footer-nav a + a { margin-left: 34px; }
  .footer-brand {
    position: absolute; right: 22px; top: 80px;
    font-size: 24px; font-weight: 700; color: var(--footer-text);
  }
  .copyright {
    position: absolute; left: 0; right: 0; bottom: 6px;
    text-align: center; font-size: 12px;
  }
</style>
</head>
<body>
  <header class="site-header">
    <div class="brand">Brackenfold Health</div>
    <a class="social-link" href="#" aria-label="Social page"></a>
    <nav class="main-nav">
      <a class="nav-locations" href="#">Locations</a>
      <a class="nav-practitioners" href="#">Practitioners</a>
      <a class="nav-physio" href="#">Physiotherapy<br>services</a>
      <a class="nav-psych" href="#">Psychology<br>services</a>
      <a class="nav-blog" href="#">Blog</a>
      <a class="nav-contact" href="#">Contact us</a>
    </nav>
  </header>

  <section class="hero">
    <div class="hero-photo" role="img" aria-label="Physiotherapist stretching the arm of a patient lying on a treatment table"></div>
    <h1 class="hero-tagline" style="font-weight:400">
      <span>We treat world class athlete</span>
      <span>&amp; see our selves as leaders in the field</span>
    </h1>
    <div class="appointment">
      <p>Request an appointment</p>
      <a class="appointment-button" href="#">Here</a>
    </div>
  </section>

  <section class="services">
    <h2 class="services-title">Services</h2>

    <article class="service-card card-group">
      <div class="service-photo photo-group" role="img" aria-label="Group therapy session with people seated in a circle"></div>
      <h3 class="service-label">Group therapy</h3>
      <p class="service-text">Therapist will provide assessment, diagnosis, education, treatment and rehabilitation for your problem,</p>
    </article>

    <article class="service-card card-therapy">
      <div class="service-photo photo-therapy" role="img" aria-label="Client talking with a therapist in a counselling room"></div>
      <h3 class="service-label">Therapy</h3>
      <p class="service-text">Therapist will provide assessment, diagnosis, education, treatment and rehabilitation for your problem,</p>
    </article>

    <article class="service-card card-physio">
      <div class="service-photo photo-physio" role="img" aria-label="Physiotherapist guiding a patient through a balance exercise"></div>
      <h3 class="service-label">Physiotherapy</h3>
      <p class="service-text">Therapist will provide assessment, diagnosis, education, treatment and rehabilitation for your problem,</p>
    </article>

    <article class="service-card card-sports">
      <div class="service-photo photo-sports" role="img" aria-label="Sports physiotherapist treating an athlete on a table"></div>
      <h3 class="service-label">Sports physiotherapy</h3>
      <p class="service-text">Therapist will provide assessment, diagnosis, education, treatment and rehabilitation for your problem,</p>
    </article>
  </section>

  <footer class="site-footer">
    <nav class="footer-nav">
      <a href="#">Locations</a>
      <a href="#">Practitioners</a>
      <a href="#">Physiotherapy<br>services</a>
      <a href="#">Psychology<br>services</a>
      <a href="#">Blog</a>
      <a href="#">Contact us</a>
    </nav>
    <div class="footer-brand">Brackenfold Health</div>
    <p class="copyright">Copyright 2014</p>
  </footer>
</body>
</html>
```